Palvanor Lending. Website design for a mortgage company.

We need a simple, but classy and artistic website design. The website should contain a home page, about page, and information page. I would like the design for each page created and I can add the content.

Palvanor Lending is a retail mortgage broker business specially crafted to provide simple, transparent, and comprehensive mortgage solutions. We understand the complexities of mortgage acquisition and have aligned with the best partners and resources to analyze the information and deliver precise, transparent, efficient, and reliable results.

Target Market(s)

We are targeting people ages 30-65 within the United States, both male and female. We are also targeting business owners and property investors specifically.

Industry/Entity Type

Mortgage Brokerage

Coding

Coded - Design and coding required

Number of Pages Required

5+ page

Font styles to use
Sans Serif
Script

Requirements
Must have
• The main purpose of this website is to provide clients with the necessary information to want to move forward with a loan transaction. The website will be informational to promote the company and showcase our purpose. The company purpose is to provide efficient and comprehensive service to clients, and to help them navigate the challenging mortgage world.

The website must mimic that of the major fortune 500 companies. It needs to be super clean, but very modern. The pictures should be of families with brown skin mostly.

The website needs to be mobile responsive. Each page needs to consist of large and responsive Hero Images. There will be background videos on the product and process pages of the website.

The website must have a semi-flat design.
The website must have a Hamburger Menu instead of a visible navigation menu.

Use the script font styles for the headlines and the sans serif for body text.

We need to have the following pages:
Home

Products

Process

About

Contact - I want a map of our office location and region. We are located in Bowie MD and our region consists of the following states: Florida, Texas, Virginia, Maryland, and Washington DC.

```html
<!DOCTYPE html>
<html lang="en">
<head>
<meta charset="utf-8">
<title>Palvanor Lending</title>
<link href="https://fonts.googleapis.com/css2?family=Roboto:wght@400;500;700&family=Lobster&family=Playball&display=swap" rel="stylesheet">
<style>
:root{
  --backdrop:#000000;
  --tint:#e9edf5;
  --white:#ffffff;
  --blue:#1856b8;
  --blue-light:#2a6ad0;
  --ink:#222222;
  --ink-soft:#555555;
  --muted:#9a9a9a;
  --dark:#353535;
  --footer:#2b2b2b;
  --line:#e6e6e6;
  --bar-blue:#29a6e8;
  --bar-light:#8fd3f5;
  --bar-green:#5cc27c;
  --bar-red:#e07b6a;
  --texas:#4ab9ec;
  --florida:#f7cf4a;
  --virginia:#7cc21f;
  --maryland:#f19a1b;
  --dc:#9d8df0;
}
*{margin:0;padding:0;box-sizing:border-box}
html,body{width:681px;height:1200px;overflow:hidden;background:var(--backdrop)}
body{font-family:'Roboto',Arial,sans-serif;color:var(--ink)}
.stage{position:absolute;left:0;top:0;width:1456px;height:2587px;transform-origin:0 0;transform:scale(0.46772,0.46386)}
.abs{position:absolute}
.t{position:absolute;line-height:1;white-space:nowrap}
.script{font-family:'Lobster',cursive;font-weight:400}
.hero-script{font-family:'Playball',cursive}

.band-top{left:81px;top:81px;width:1294px;height:682px;background:var(--tint)}
.band-white{left:81px;top:763px;width:1294px;height:463px;background:var(--white)}
.band-tint{left:81px;top:1226px;width:1294px;height:369px;background:var(--tint)}
.band-sky{left:81px;top:1595px;width:1294px;height:837px;background:linear-gradient(180deg,#eef3f8 0%,#f8fafc 25%,#ffffff 50%)}
.site-footer{left:81px;top:2432px;width:1294px;height:54px;background:var(--footer)}

.brand{left:333px;top:113px;font-size:25px;font-weight:500;letter-spacing:.3px;color:var(--ink)}
.menu-icon{left:1096px;top:124px}

.hero-photo{left:333px;top:190px;width:435px;height:371px;background:linear-gradient(180deg,#9ec3e6 0%,#c9dcef 35%,#8a6a52 55%,#6d5642 70%,#4f7a2a 85%,#3f6a22 100%)}
.hero-panel{left:768px;top:190px;width:354px;height:371px;background:var(--blue);overflow:hidden}
.hero-title{left:797px;top:240px;font-size:34px;line-height:41px;color:var(--white);white-space:nowrap}
.hero-sub{left:797px;top:380px;font-size:14px;line-height:20px;color:var(--white)}
.hero-btn{left:798px;top:443px;width:126px;height:30px;border-radius:15px;background:var(--ink);color:var(--white);font-size:10px;font-weight:500;display:flex;align-items:center;justify-content:center;letter-spacing:.3px}
.hero-next{left:740px;top:505px}

.why-title{left:528px;top:606px;width:400px;text-align:center;font-size:27px;color:var(--ink)}
.why-text{left:528px;top:650px;width:400px;text-align:center;font-size:12.5px;line-height:18px;color:var(--ink)}

.section-title{width:1294px;left:81px;text-align:center;font-size:40px;color:var(--ink)}

.donut{left:330px;top:952px}
.donut-num{left:330px;top:1005px;width:160px;text-align:center;font-size:34px;font-weight:700;color:#333}
.donut-label{left:330px;top:1041px;width:160px;text-align:center;font-size:16px;color:#555}
.target-title{left:507px;top:936px;font-size:22px;font-weight:500;color:var(--ink)}
.legend{left:511px;top:979px;font-size:14px;color:var(--muted)}
.legend li{list-style:none;height:22.7px;display:flex;align-items:center;gap:4px}
.legend .sw{width:11px;height:11px;border-radius:2px;display:inline-block}
.legend .pct{margin-left:10px}

.problems{left:746px;top:923px;width:376px;height:223px;background:var(--blue);color:var(--white)}
.box-title{position:absolute;left:24px;font-size:24px;font-weight:500;line-height:1}
.problems .box-title{top:24px}
.problems ol{position:absolute;left:24px;top:68px;list-style:none;font-size:15px;line-height:28.3px}

.solution{left:332px;top:1290px;width:347px;height:236px;background:var(--blue);color:var(--white)}
.solution .box-title{top:24px}
.solution p{position:absolute;left:24px;top:64px;width:305px;font-size:15.5px;line-height:25px}

.compare{left:692px;top:1290px;width:430px;border-collapse:collapse;background:var(--white);font-size:11px;color:var(--ink)}
.compare th{background:var(--dark);color:var(--white);font-weight:700;text-align:left;height:46px;padding-left:17px;font-size:11px}
.compare td{height:38.6px;padding-left:17px;border-top:1px solid var(--line)}
.compare th:first-child,.compare td:first-child{width:155px;border-right:1px solid var(--line)}

.house-art{left:120px;top:1680px;width:530px;height:310px;border-radius:40px;background:radial-gradient(ellipse at 50% 45%,#c7a37e 0%,#b48b64 28%,#8fb36a 55%,rgba(200,225,190,.5) 75%,rgba(255,255,255,0) 100%)}
.channels{left:652px;top:1722px;width:329px;height:300px;background:var(--dark);color:var(--white)}
.channels .box-title{top:33px}
.channels ol{position:absolute;left:23px;top:84px;list-style:none;font-size:15px;line-height:29.8px;color:#e2e2e2}
.activities{left:997px;top:1722px;width:328px;height:300px;background:var(--tint);color:var(--ink)}
.activities .box-title{top:33px}
.activities p{position:absolute;left:24px;top:80px;width:290px;font-size:16px;line-height:24.3px;color:#333}

.chart-card{top:2166px;width:252px;height:214px;background:var(--white);border:1px solid #ececec;box-shadow:0 1px 4px rgba(0,0,0,.06)}
.chart-card svg{position:absolute;left:0;top:0}
.chart-svg text{font-family:'Roboto',Arial,sans-serif}

.copyright{left:333px;top:2454px;font-size:10.5px;color:#d0d0d0}
.legal{left:939px;top:2454px;font-size:10.5px;color:#d0d0d0}
.legal .link-u{text-decoration:underline}
.legal .sep{margin:0 12px;color:#999}
</style>
</head>
<body>
<div class="stage">
  <div class="abs band-top"></div>
  <div class="abs band-white"></div>
  <div class="abs band-tint"></div>
  <div class="abs band-sky"></div>
  <div class="abs site-footer"></div>

  <header>
    <div class="t brand">PALVANOR LENDING</div>
    <svg class="abs menu-icon" width="26" height="20" viewBox="0 0 26 20" aria-label="Menu">
      <rect x="0" y="0" width="26" height="2.4" fill="#1a5bbd"/>
      <rect x="0" y="8" width="26" height="2.4" fill="#1a5bbd"/>
      <rect x="0" y="16" width="26" height="2.4" fill="#1a5bbd"/>
    </svg>
  </header>

  <section class="hero">
    <div class="abs hero-photo" role="img" aria-label="Photo of a large brick family home with green lawn under a blue sky"></div>
    <div class="abs hero-panel">
      <svg width="354" height="371" viewBox="0 0 354 371">
        <polygon points="90,0 354,0 354,80 300,165" fill="#2264c6" opacity=".7"/>
        <polygon points="150,250 354,180 354,371 230,371" fill="#2a6bcc" opacity=".55"/>
        <polygon points="0,300 120,371 0,371" fill="#1d5cbf" opacity=".6"/>
      </svg>
    </div>
    <div class="t hero-title hero-script">Big Dreams<br>Even Bigger and<br>Better Loans</div>
    <div class="t hero-sub">An intelligent way to make your<br>dreams come true!</div>
    <div class="abs hero-btn">PRODUCTS</div>
    <svg class="abs hero-next" width="100" height="60" viewBox="0 0 100 60">
      <path d="M0,56 C20,56 26,20 50,20 C74,20 80,56 100,56 L100,60 L0,60 Z" fill="#eef1f7"/>
      <circle cx="50" cy="40" r="18" fill="#1856b8"/>
      <path d="M47,33 L54,40 L47,47" stroke="#fff" stroke-width="2.4" fill="none" stroke-linecap="round" stroke-linejoin="round"/>
    </svg>
  </section>

  <section class="why">
    <h2 class="t why-title script">Why Palvanor Lending</h2>
    <p class="abs why-text">Palvanor Lending is a retail mortgage broker business specially crafted to provide simple, transparent, and comprehensive mortgage solutions.</p>
  </section>

  <section class="opportunity">
    <h2 class="t section-title script" style="top:818px">Our Opportunity</h2>
    <svg class="abs donut" width="160" height="160" viewBox="0 0 160 160">
      <g transform="rotate(-90 80 80)" fill="none" stroke-width="23">
        <circle cx="80" cy="80" r="66.5" pathLength="100" stroke="var(--texas)" stroke-dasharray="41 59" stroke-dashoffset="0"/>
        <circle cx="80" cy="80" r="66.5" pathLength="100" stroke="var(--florida)" stroke-dasharray="34 66" stroke-dashoffset="-41"/>
        <circle cx="80" cy="80" r="66.5" pathLength="100" stroke="var(--virginia)" stroke-dasharray="15 85" stroke-dashoffset="-75"/>
        <circle cx="80" cy="80" r="66.5" pathLength="100" stroke="var(--maryland)" stroke-dasharray="9 91" stroke-dashoffset="-90"/>
        <circle cx="80" cy="80" r="66.5" pathLength="100" stroke="var(--dc)" stroke-dasharray="1.5 98.5" stroke-dashoffset="-98.5"/>
      </g>
      <circle cx="80" cy="80" r="55" fill="#fff"/>
    </svg>
    <div class="t donut-num">867K</div>
    <div class="t donut-label">Prospects</div>

    <h3 class="t target-title">Target market</h3>
    <ul class="abs legend">
      <li><span class="sw" style="background:var(--texas)"></span>Texas<span class="pct">41% ($85.7B)</span></li>
      <li><span class="sw" style="background:var(--florida)"></span>Florida<span class="pct">34% ($77.6B)</span></li>
      <li><span class="sw" style="background:var(--virginia)"></span>Virginia<span class="pct">15% ($37.3B)</span></li>
      <li><span class="sw" style="background:var(--maryland)"></span>Maryland<span class="pct">9% ($24.3B)</span></li>
      <li><span class="sw" style="background:var(--dc)"></span>District of Columbia<span class="pct">1% ($5.2B)</span></li>
    </ul>

    <div class="abs problems">
      <h3 class="box-title">Problems worth solving</h3>
      <ol>
        <li>1. Understanding complex mortgage terms.</li>
        <li>2. Lack of transparent communication.</li>
        <li>3. Improper expectation setting.</li>
        <li>4. Getting quick and reliable results.</li>
        <li>5. Shopping for the best mortgage rates.</li>
      </ol>
    </div>
  </section>

  <section class="solution-block">
    <div class="abs solution">
      <h3 class="box-title">Our solution</h3>
      <p>We understand the complexities of mort-gage acquisition and have aligned with the best partners and resources to analyze the information and deliver precise, transpar-ent, ecient, and reliable results.</p>
    </div>
    <table class="abs compare">
      <thead><tr><th>COMPETITORS</th><th>HOW OUR SOLUTION IS BETTER</th></tr></thead>
      <tbody>
        <tr><td>Steadfast Rate</td><td>Higher service level</td></tr>
        <tr><td>Alder Brook Mortgage</td><td>More broad loan selection</td></tr>
        <tr><td>Loan Works</td><td>Customized process approach</td></tr>
        <tr><td>Orin Home Loans</td><td>Transparent workow</td></tr>
        <tr><td>Homelytic.com</td><td>Greater exibility</td></tr>
      </tbody>
    </table>
  </section>

  <section class="sales">
    <h2 class="t section-title script" style="top:1645px">Sales and Marketing</h2>
    <div class="abs house-art" role="img" aria-label="Illustration of a cutaway two-storey house on a grassy island with trees and numbered markers"></div>
    <div class="abs channels">
      <h3 class="box-title">Sales Channels</h3>
      <ol>
        <li>1. Eective Search Engine Optimization SEO</li>
        <li>2. Digital training solutions</li>
        <li>3. Interactive online webinars</li>
        <li>4. Strategic partnerships</li>
        <li>5. Group networking seminars</li>
      </ol>
    </div>
    <div class="abs activities">
      <h3 class="box-title">Marketing Activities</h3>
      <p>Utilizing eective search engine optimi-zation, we will position our website to be visible to consumers seeking specic loan products. Aligning with in-novative partners, we will expose ourselves to prospects during in-person and digital training.</p>
    </div>
  </section>

  <section class="financials">
    <h2 class="t section-title script" style="top:2082px">Financial Projections</h2>

    <div class="abs chart-card" style="left:333px">
      <svg class="chart-svg" width="252" height="214" viewBox="0 0 252 214">
        <g fill="var(--bar-blue)">
          <rect x="22" y="122" width="24" height="17"/>
          <rect x="67" y="44" width="24" height="95"/>
          <rect x="113" y="30" width="24" height="109"/>
        </g>
        <line x1="10" y1="139" x2="242" y2="139" stroke="#9a9a9a" stroke-width="2"/>
        <g font-size="9" font-weight="700" text-anchor="middle" fill="#222">
          <text x="34" y="116">$162K</text><text x="79" y="38">$811K</text><text x="125" y="24">$932K</text>
          <text x="171" y="134">$0</text><text x="217" y="134">$0</text>
        </g>
        <g font-size="12" font-weight="700" text-anchor="middle" fill="#333">
          <text x="33" y="159">FY'21</text><text x="79" y="159">FY'22</text><text x="125" y="159">FY'23</text><text x="171" y="159">FY'24</text><text x="217" y="159">FY'25</text>
        </g>
        <text x="125" y="186" font-size="16" font-weight="700" text-anchor="middle" fill="#222">Revenue</text>
      </svg>
    </div>

    <div class="abs chart-card" style="left:606px">
      <svg class="chart-svg" width="252" height="214" viewBox="0 0 252 214">
        <g fill="var(--bar-light)" stroke="var(--bar-blue)" stroke-width="1">
          <rect x="20" y="104" width="24" height="8"/>
          <rect x="67" y="76" width="24" height="36"/>
          <rect x="114" y="70" width="24" height="42"/>
        </g>
        <line x1="10" y1="112" x2="242" y2="112" stroke="#9a9a9a" stroke-width="2"/>
        <g font-size="9" font-weight="700" text-anchor="middle" fill="#222">
          <text x="32" y="98">$69K</text><text x="79" y="70">$303K</text><text x="126" y="64">$347K</text>
          <text x="172" y="106">$10K</text><text x="219" y="106">$10K</text>
        </g>
        <g font-size="12" font-weight="700" text-anchor="middle" fill="#333">
          <text x="32" y="132">FY'21</text><text x="79" y="132">FY'22</text><text x="126" y="132">FY'23</text><text x="172" y="132">FY'24</text><text x="219" y="132">FY'25</text>
        </g>
        <text x="126" y="159" font-size="16" font-weight="700" text-anchor="middle" fill="#222">Expenses &amp; Costs</text>
      </svg>
    </div>

    <div class="abs chart-card" style="left:879px">
      <svg class="chart-svg" width="252" height="214" viewBox="0 0 252 214">
        <g fill="var(--bar-green)">
          <rect x="24" y="72" width="24" height="5"/>
          <rect x="69" y="48" width="24" height="29"/>
          <rect x="115" y="44" width="24" height="33"/>
        </g>
        <g fill="var(--bar-red)">
          <rect x="161" y="77" width="24" height="2"/>
          <rect x="206" y="77" width="24" height="2"/>
        </g>
        <line x1="12" y1="77" x2="240" y2="77" stroke="#9a9a9a" stroke-width="2"/>
        <g font-size="9" font-weight="700" text-anchor="middle" fill="#222">
          <text x="36" y="66">$93K</text><text x="81" y="42">$508K</text><text x="127" y="38">$586K</text>
          <text x="172" y="92">($10K)</text><text x="218" y="92">($10K)</text>
        </g>
        <g font-size="12" font-weight="700" text-anchor="middle" fill="#333">
          <text x="36" y="155">FY'21</text><text x="81" y="155">FY'22</text><text x="127" y="155">FY'23</text><text x="172" y="155">FY'24</text><text x="218" y="155">FY'25</text>
        </g>
        <text x="127" y="181" font-size="16" font-weight="700" text-anchor="middle" fill="#222">Profit</text>
      </svg>
    </div>
  </section>

  <footer>
    <div class="t copyright">© &nbsp;Copyright 2020 All Right Reserved.</div>
    <div class="t legal"><span class="link-u">Privacy Statement</span><span class="sep">|</span><span>Terms Of Use</span></div>
  </footer>
</div>
</body>
</html>
```